依頼詳細
会社の名刺デザインを新規に作成しようと思っています。
名刺の背景は白地になります。シンプルなデザインですが、目に止まるようにして頂きたいです。
裏面にロゴマークを大きくバックに入れたいと思っております。
記載項目
表面:会社名/役職/住所/電話/Fax/Mail
裏面:事業内容
希望イメージ
シンプル 複雑
単色 カラフル
暗い 明るい
日常 高級
遊び心 厳粛
未来的 伝統的
女性的 男性的
希望する色
青、黒、緑、銀、
納品ファイル
• 高解像度JPG (.jpg)
• イラストレーター形式 (.ai)
• フォトショップ形式 (.psd)
補足説明
若くて元気な会社です。そのようなイメージも名刺で表現出来ればと思ってます。
失礼しました。会社名は、「株式会社ザルノクラッセ」です。
名刺の裏面に大きくロゴマークのみを入れて、その上に重なるように事業内容などを書き込みたいと思っております。

シンプルかつ存在感のあるデザインが気に入りました。

色々とありがとうございます。また何かありました際は、ぜひ宜しくお願いします。

```html
<!DOCTYPE html>
<html lang="ja">
<head>
<meta charset="UTF-8">
<title>ザルノクラッセ 名刺デザイン</title>
<link href="https://fonts.googleapis.com/css2?family=Noto+Sans+JP:wght@400;500;700&family=Noto+Serif+JP:wght@400;500&display=swap" rel="stylesheet">
<style>
  :root {
    --blue-deep: #0f6fb8;
    --blue-mid: #2a9ad6;
    --blue-light: #8fd0ef;
    --ink: #1d1d1f;
    --ink-soft: #4a4a4e;
    --paper: #ffffff;
    --backdrop: #eeeff1;
  }
  * { margin: 0; padding: 0; box-sizing: border-box; }
  html, body { width: 900px; height: 1200px; overflow: hidden; }
  body {
    background: var(--backdrop);
    font-family: "Noto Sans JP", sans-serif;
    color: var(--ink);
    position: relative;
  }
  .card {
    position: absolute;
    left: 60px;
    width: 780px;
    height: 490px;
    background: var(--paper);
    box-shadow: 0 4px 14px rgba(0,0,0,0.18);
    overflow: hidden;
  }
  .card--front { top: 50px; }
  .card--back { top: 660px; }
  .card__swoosh { position: absolute; inset: 0; width: 100%; height: 100%; }

  /* front */
  .holder { position: absolute; top: 62px; left: 390px; display: flex; align-items: flex-start; }
  .holder__title { font-size: 15px; color: var(--ink-soft); margin-top: 14px; margin-right: 14px; letter-spacing: 0.05em; }
  .holder__rule { width: 3px; height: 58px; background: linear-gradient(var(--blue-mid), var(--blue-light)); margin-right: 14px; }
  .holder__name { font-size: 34px; font-weight: 500; letter-spacing: 0.08em; line-height: 1.2; }
  .holder__roman { font-size: 14px; color: var(--ink-soft); margin-top: 4px; letter-spacing: 0.04em; }

  .brand { display: flex; align-items: center; gap: 14px; }
  .brand__dot { border-radius: 50%; background: var(--blue-mid); flex: none; }
  .brand__name { font-family: "Noto Serif JP", serif; font-weight: 400; color: var(--ink); letter-spacing: 0.02em; }
  .card--front .brand { position: absolute; left: 84px; top: 200px; }
  .card--front .brand__dot { width: 40px; height: 40px; }
  .card--front .brand__name { font-size: 40px; }

  .company { position: absolute; left: 84px; top: 290px; }
  .company__name { font-size: 20px; font-weight: 700; margin-bottom: 8px; letter-spacing: 0.02em; }
  .company__line { font-size: 14px; line-height: 1.7; color: var(--ink); }

  /* back */
  .card--back .brand { position: absolute; left: 0; right: 0; top: 80px; flex-direction: column; gap: 18px; }
  .card--back .brand__dot { width: 120px; height: 120px; background: radial-gradient(circle at 35% 35%, var(--blue-light), var(--blue-deep)); }
  .card--back .brand__name { font-size: 40px; }
  .services { position: absolute; top: 318px; left: 0; right: 0; text-align: center; }
  .services__heading { font-size: 14px; letter-spacing: 0.9em; padding-left: 0.9em; font-weight: 500; }
  .services__rule { width: 250px; height: 2px; margin: 12px auto 14px; background: linear-gradient(90deg, var(--blue-light), var(--blue-deep), var(--blue-light)); }
  .services__list { list-style: none; display: inline-block; text-align: left; font-size: 15px; line-height: 1.75; }
  .services__list li::before { content: "■"; margin-right: 2px; }
</style>
</head>
<body>

<section class="card card--front" aria-label="名刺 表面">
  <svg class="card__swoosh" viewBox="0 0 780 490" aria-hidden="true">
    <defs>
      <linearGradient id="swoopFront" x1="0" y1="0" x2="1" y2="1">
        <stop offset="0" stop-color="#0f6fb8"/>
        <stop offset="1" stop-color="#35aee0"/>
      </linearGradient>
    </defs>
    <path d="M0,0 H370 Q110,40 0,250 Z" fill="url(#swoopFront)"/>
    <path d="M0,0 H300 Q90,55 0,215 Z" fill="#8fd0ef" opacity="0.55"/>
    <path d="M0,0 H250 Q70,60 0,180 Z" fill="#ffffff"/>
    <path d="M780,490 H520 Q720,420 780,230 Z" fill="url(#swoopFront)"/>
    <path d="M780,490 H590 Q750,430 780,310 Z" fill="#ffffff" opacity="0.35"/>
  </svg>

  <div class="holder">
    <p class="holder__title">代表取締役</p>
    <span class="holder__rule"></span>
    <div>
      <p class="holder__name">佐藤 健太</p>
      <p class="holder__roman">Sato Kenta</p>
    </div>
  </div>

  <div class="brand">
    <span class="brand__dot"></span>
    <span class="brand__name">Zarno Classe</span>
  </div>

  <div class="company">
    <p class="company__name">株式会社ザルノクラッセ</p>
    <p class="company__line">〒000-0000　○○県○○市○○町00-000</p>
    <p class="company__line">TEL／000-000-0000　FAX／000-000-0000</p>
    <p class="company__line">E-mail／info@zarno-classe.jp</p>
  </div>
</section>

<section class="card card--back" aria-label="名刺 裏面">
  <svg class="card__swoosh" viewBox="0 0 780 490" aria-hidden="true">
    <defs>
      <linearGradient id="swoopBack" x1="0" y1="0" x2="1" y2="1">
        <stop offset="0" stop-color="#35aee0"/>
        <stop offset="1" stop-color="#0f6fb8"/>
      </linearGradient>
    </defs>
    <path d="M0,0 H230 Q60,30 0,170 Z" fill="url(#swoopBack)"/>
    <path d="M0,0 H160 Q40,40 0,120 Z" fill="#ffffff"/>
    <path d="M500,0 H780 V490 H720 Q780,170 500,0 Z" fill="url(#swoopBack)"/>
    <path d="M580,0 H780 V490 H760 Q790,160 580,0 Z" fill="#8fd0ef" opacity="0.45"/>
  </svg>

  <div class="brand">
    <span class="brand__dot"></span>
    <span class="brand__name">Zarno Classe</span>
  </div>

  <div class="services">
    <p class="services__heading">事業内容</p>
    <div class="services__rule"></div>
    <ul class="services__list">
      <li>ビルメンテナンス</li>
      <li>工事</li>
      <li>○○事業</li>
    </ul>
  </div>
</section>

</body>
</html>
```